Hot-air ballooning company needs a DL-size flyer

Skylark Aerial Tours is a hot-air ballooning company which flies passengers in the King Valley, Victoria, Australia.
We need a 2-sided DL-size flyer which promotes our hot-air balloon flights and packages.
Most of our customers are couples, and we want the flyer design to communicate safety, adventure, and romance.
The flyer should make the best use of our images which we provide, and we've also included a document with the text for the flyer.
Updates

2 days is not long enough to gather designs, the brief never asked me what my deadline should be.

Target Market(s)

Couples, buyers are majority female, between the ages of 20-60

Industry/Entity Type

Tourism

Font styles to use
Sans Serif

Colors

Designer to choose colors to be used in the design.

Requirements
Must have
• Communicate safety, adventure, and romance
• Use images
Nice to have
• There is a lot of text, it would be great if you could make it look like as little text as possible
Should not have
• No childish designs

```html
<!DOCTYPE html>
<html lang="en">
<head>
<meta charset="utf-8">
<title>King Valley Hot-Air Ballooning</title>
<link rel="stylesheet" href="https://fonts.googleapis.com/css2?family=Raleway:wght@200;300&family=Nunito+Sans:wght@400&display=swap">
<style>
  :root {
    --sky-top: #2c78b9;
    --sky-mid: #6fa6d2;
    --sky-low: #a9c6dc;
    --mist: #c8cfd1;
    --haze: #9aa79a;
    --orchard: #6d7048;
    --ground: #4e5a33;
    --ink-light: #ffffff;
    --rule: rgba(255, 255, 255, 0.92);
  }
  * { margin: 0; padding: 0; box-sizing: border-box; }
  html, body { width: 1200px; height: 566px; overflow: hidden; background: #ffffff; }
  .flyer {
    position: relative;
    width: 1200px;
    height: 566px;
    overflow: hidden;
    color: var(--ink-light);
    font-family: "Nunito Sans", "Helvetica Neue", Arial, sans-serif;
  }
  .scene-photo {
    position: absolute;
    inset: 0;
    background: linear-gradient(180deg,
      var(--sky-top) 0%,
      var(--sky-mid) 30%,
      var(--sky-low) 52%,
      var(--mist) 62%,
      var(--haze) 72%,
      var(--orchard) 84%,
      var(--ground) 100%);
  }
  .title-block {
    position: absolute;
    left: 46px;
    top: 45px;
    width: 598px;
    height: 245px;
  }
  .title-block svg { display: block; overflow: visible; }
  .title-text {
    font-family: "Raleway", "Helvetica Neue", Arial, sans-serif;
    fill: var(--ink-light);
  }
  .title-kicker { font-weight: 300; font-size: 33px; }
  .title-main { font-weight: 200; font-size: 156px; }
  .title-sub { font-weight: 200; font-size: 98px; }
  .tagline {
    position: absolute;
    left: 46px;
    top: 347px;
    width: 598px;
    height: 40px;
    border: 1.5px solid var(--rule);
    display: flex;
    align-items: center;
    justify-content: center;
    font-family: "Raleway", "Helvetica Neue", Arial, sans-serif;
    font-weight: 300;
    font-size: 19.5px;
    letter-spacing: 0.6px;
    white-space: nowrap;
  }
  .intro {
    position: absolute;
    left: 708px;
    top: 64px;
    width: 418px;
    font-size: 14.4px;
    line-height: 20.2px;
    text-align: justify;
  }
  .intro p + p { margin-top: 20px; }
</style>
</head>
<body>
  <main class="flyer">
    <div class="scene-photo" role="img" aria-label="Dawn aerial view of hot-air balloons drifting over misty King Valley vineyards, trees and a country lodge"></div>

    <header class="title-block">
      <svg width="598" height="245" viewBox="0 0 598 245" aria-labelledby="title-label">
        <title id="title-label">King Valley Hot-Air Ballooning</title>
        <g fill="none" stroke="#ffffff" stroke-width="1.5">
          <path d="M20 1 H1 V244 H20"/>
          <path d="M578 1 H597 V244 H578"/>
        </g>
        <text class="title-text title-kicker" x="299" y="36" text-anchor="middle">KING VALLEY</text>
        <text class="title-text title-main" x="40" y="168" textLength="552" lengthAdjust="spacingAndGlyphs">HOT-AIR</text>
        <text class="title-text title-sub" x="42" y="243" textLength="550" lengthAdjust="spacingAndGlyphs">BALLOONING</text>
      </svg>
    </header>

    <div class="tagline">THE PERFECT GOURMET BALLOONING EXPERIENCE</div>

    <section class="intro">
      <p>Live the romance and adventure of flying the beautiful King Valley and surrounds in a hot-air balloon at dawn. From the vineyards and patchwork of fields the views expand to the Ovens River, spectacular Mt Buffalo and the High Country beyond. The mountain views, once aloft, come to life in dramatic 3D with the early morning light. Celebrate your flight with a delicious breakfast afterwards (optional)</p>
      <p>Milawa is conveniently located less than an hour’s drive from most places in Victoria’s North East and Albury in NSW. Mansfield flights are also available.</p>
    </section>
  </main>
</body>
</html>
```